Seriöser Briefkopf für Rechtsanwaltskanzlei
Zielgruppe
Rechtsanwaltskanzlei
Aufgabenstellung
Benötigt wird ein seriöser Briefkopf für eine Anwaltskanzlei. Er soll im Wesentlichen aus Typen bestehen, mit denen aber durchaus 'gespielt' werden soll (Groß- und Kleinschreibung, querstehend, angeschnitten o.Ä)
Folgender Inhalt muss untergebracht werden:
Rechtsanwaltskanzlei Kessenhagen
Rechtsanwalt Dipl.-Ing. Udo Kessenhagen
Rechtsanwalt Matthias Wendel
Der Briefkopf muss schwarz-weiß druckbar sein und beim Versenden per Fax müssen alle Daten gut lesbar bleiben (also keine Grautöne bei Tel-Nr. o.Ä.)
Der Briefkopf soll mit einem Drucker ausgedruckt werden, sodass keine Gestaltung bis zum Blattrand gehen darf.
Bitte keine Logos mit Paragrafen-Zeichen oder Justitia und nicht die Abkürzung RUK verwenden.
Keine - Einfach drauflos - Ich bin gespannt

```html
<!DOCTYPE html>
<html lang="de">
<head>
<meta charset="utf-8">
<title>Briefkopf – Rechtsanwaltskanzlei Kessenhagen</title>
<link rel="stylesheet" href="https://fonts.googleapis.com/css2?family=EB+Garamond:wght@400;500&display=swap">
<style>
  :root {
    --ink: #111111;
    --rule: #555555;
    --paper: #ffffff;
  }
  html, body {
    margin: 0;
    padding: 0;
    overflow: hidden;
    background: var(--paper);
  }
  .letterhead {
    position: relative;
    width: 849px;
    height: 1200px;
    background: var(--paper);
    color: var(--ink);
    font-family: "EB Garamond", Georgia, serif;
    overflow: hidden;
  }
  .firm-name {
    margin: 0;
    font-weight: 500;
    color: var(--ink);
  }
  .firm-name__kind,
  .firm-name__surname {
    position: absolute;
    left: 0;
    width: 100%;
    text-align: center;
    line-height: 1;
    white-space: nowrap;
  }
  .firm-name__kind {
    top: 47px;
    font-size: 17px;
    letter-spacing: 2.6px;
  }
  .firm-name__surname {
    top: 69px;
    font-size: 25px;
    letter-spacing: 2.4px;
    text-transform: uppercase;
  }
  .rule {
    position: absolute;
    left: 81px;
    width: 689px;
    height: 0;
    border-top: 0.8px solid var(--rule);
  }
  .rule--top { top: 98px; }
  .rule--bottom { top: 1170px; }
  .partners {
    position: absolute;
    top: 103px;
    left: 0;
    width: 100%;
    margin: 0;
    padding: 0;
    list-style: none;
    text-align: center;
    font-size: 12px;
    line-height: 13px;
  }
  .contact {
    position: absolute;
    top: 1176px;
    left: 0;
    width: 100%;
    margin: 0;
    text-align: center;
    font-size: 11px;
    line-height: 14px;
    letter-spacing: 0.1px;
    white-space: nowrap;
  }
  .contact .sep { margin: 0 3px; }
</style>
</head>
<body>
  <main class="letterhead">
    <header>
      <h1 class="firm-name">
        <span class="firm-name__kind">Rechtsanwaltskanzlei</span>
        <span class="firm-name__surname">Kessenhagen</span>
      </h1>
      <div class="rule rule--top"></div>
      <ul class="partners">
        <li>Rechtsanwalt Dipl.-Ing. Udo Kessenhagen</li>
        <li>Rechtsanwalt Matthias Wendel</li>
      </ul>
    </header>
    <footer>
      <div class="rule rule--bottom"></div>
      <p class="contact">Ahornweg 7<span class="sep">·</span>04109 Leipzig<span class="sep">·</span>Tel. 0341 55218-0<span class="sep">·</span>Fax 0341 55218-46<span class="sep">·</span>mail@kessenhagen-kanzlei.de<span class="sep">·</span>www.kessenhagen-kanzlei.de</p>
    </footer>
  </main>
</body>
</html>
```